cup design rebranding with modern design

8 oz and 4 oz cup redesign

i will share my existing cups

also i want different slogans for coffee on the back also my logo is attached any color also a design for take away holder

be creative

modern

and elegant

i need it to be innovative

Industry/Entity Type

Coffee Shop

Font styles to use
Decorative
Script

Colors

Designer to choose colors to be used in the design.

Requirements
Must have
• logo
• instagram account @marlowbrewhouse
• slogan english or arabic

```html
<!DOCTYPE html>
<html lang="en">
<head>
<meta charset="utf-8">
<title>Marlow Specialty Coffee House – Cup Wrap</title>
<link href="https://fonts.googleapis.com/css2?family=Quicksand:wght@400;500&family=Nunito:wght@600&family=Allura&display=swap" rel="stylesheet">
<style>
  :root {
    --stage: #c4c4c4;
    --wrap-dark: #231f20;
    --ink-light: #ffffff;
    --pattern-light: #e9e9e9;
    --pattern-mid: #9a9a9a;
  }
  * { margin: 0; padding: 0; box-sizing: border-box; }
  html, body {
    width: 1200px;
    height: 1000px;
    overflow: hidden;
    background: var(--stage);
  }
  .canvas {
    position: relative;
    width: 1200px;
    height: 1000px;
    background: var(--stage);
  }
  .cup-wrap {
    position: absolute;
    left: 0;
    top: 242px;
    width: 1200px;
    height: 515px;
    background: var(--wrap-dark);
    overflow: hidden;
  }
  .wave-strip {
    position: absolute;
    background: linear-gradient(160deg, var(--pattern-light) 0%, var(--pattern-mid) 45%, var(--pattern-light) 100%);
  }
  .wave-strip--front { left: 210px; top: 0; width: 188px; height: 515px; }
  .wave-strip--back { left: 807px; top: 0; width: 183px; height: 293px; }

  .brand-seal {
    position: absolute;
    left: 140px;
    top: 33px;
    width: 330px;
    height: 330px;
  }
  .brand-seal svg { position: absolute; inset: 0; }
  .brand-name {
    position: absolute;
    left: 0;
    width: 330px;
    top: 122px;
    text-align: center;
    font-family: "Quicksand", sans-serif;
    font-weight: 400;
    font-size: 54px;
    letter-spacing: 4px;
    color: var(--ink-light);
    line-height: 1;
  }
  .brand-tagline {
    position: absolute;
    left: 0;
    width: 330px;
    top: 184px;
    text-align: center;
    font-family: "Quicksand", sans-serif;
    font-weight: 400;
    font-size: 15.5px;
    letter-spacing: 0.6px;
    color: var(--ink-light);
  }

  .slogan {
    position: absolute;
    left: 788px;
    top: 306px;
    color: var(--ink-light);
  }
  .slogan__lead {
    font-family: "Nunito", sans-serif;
    font-weight: 600;
    font-size: 35px;
    line-height: 1;
    letter-spacing: -0.3px;
  }
  .slogan__tail {
    position: relative;
    height: 70px;
    margin-top: 4px;
  }
  .slogan__amp {
    position: absolute;
    left: -2px;
    top: 6px;
    font-family: "Allura", cursive;
    font-size: 44px;
    line-height: 1;
  }
  .slogan__be {
    position: absolute;
    left: 28px;
    top: 12px;
    font-family: "Quicksand", sans-serif;
    font-size: 11px;
  }
  .slogan__word {
    position: absolute;
    left: 32px;
    top: 14px;
    font-family: "Allura", cursive;
    font-size: 56px;
    line-height: 1;
    white-space: nowrap;
  }
</style>
</head>
<body>
  <main class="canvas">
    <section class="cup-wrap">
      <div class="wave-strip wave-strip--front" role="img" aria-label="Hand-drawn white swirling wave pattern on dark ground"></div>
      <div class="wave-strip wave-strip--back" role="img" aria-label="Hand-drawn white swirling wave pattern on dark ground"></div>

      <div class="brand-seal">
        <svg width="330" height="330" viewBox="0 0 330 330" aria-hidden="true">
          <circle cx="165" cy="165" r="163" fill="var(--wrap-dark)"/>
          <circle cx="165" cy="165" r="160" fill="none" stroke="var(--ink-light)" stroke-width="6"/>
          <circle cx="165" cy="165" r="146" fill="none" stroke="var(--ink-light)" stroke-width="3"/>
        </svg>
        <div class="brand-name">MARLOW</div>
        <div class="brand-tagline">SPECIALTY COFFEE HOUSE</div>
      </div>

      <div class="slogan">
        <div class="slogan__lead">Drink Coffee.</div>
        <div class="slogan__tail">
          <span class="slogan__amp">&amp;</span>
          <span class="slogan__be">be</span>
          <span class="slogan__word">Awesome</span>
        </div>
      </div>
    </section>
  </main>
</body>
</html>
```